Internationales Familienunternehmen sucht Designvorschläge für Broschüre/Folder
Zielgruppe
Unser Unternehmen besteht aus 4 aktiven Sparten:
gastrosystems | elektrosystems | servicepartner | morafi kavum crafts
Alle Sparten sollen mit einem Layout bedient werden. Ziel wäre es aber z.B. auf der Titelseite im oberen Bereich die jeweiligen Sparten erkennen zu können und das jeweilige Prospektthema klein. Sodass man z.B. in einem Prospektständer die verschiedenen Prospekte auf einen Griff unterscheiden udn entnehmen kann.
Das Design muss verschiedenen Zielgruppen gefallen, daher muss das Layout modern, jung und dem neuen Logo entsprechend sein.
Aufgabenstellung
Wir haben unser Logo mit Anfang 2014 einem kompletten Redesign unterzogen und benötigen jetzt ein modernes und ansprechendes "passendes" Layout für unsere Produktbroschüren und -folder. Gesucht ist also Layoutvorschlag für Umschlag und Innenteil zur Präsentation von Produkten, Referenzen und natürlich entsprechenden Textflächen.
Als Ideenvolage kann unsere derzeit entstehende Website dienen: http://new.kavum.net/
Bitte NICHT (!!!) an unserer bestehenden Website orientieren. www.kavum.net ist nur noch kurze Zeit online!!! ACHTUNG!!!

```html
<!DOCTYPE html>
<html lang="de">
<head>
<meta charset="utf-8">
<title>Gastroschankanlagen – MORAFI NG Full-Color-Touch</title>
<link href="https://fonts.googleapis.com/css2?family=Open+Sans:wght@400;600&display=swap" rel="stylesheet">
<style>
  :root {
    --bg: #e9e9e9;
    --paper: #ffffff;
    --accent: #e05a1e;
    --dark: #2f2f2f;
    --heading-grey: #555555;
    --text: #444444;
    --device-light: #e4e6e9;
    --device-mid: #b9bdc3;
    --photo-dark: #1c120c;
    --photo-copper: #a8582a;
    --photo-light: #e8c6a4;
  }
  * { margin: 0; padding: 0; box-sizing: border-box; }
  html, body {
    width: 968px; height: 1200px; overflow: hidden;
    background: var(--bg);
    font-family: "Open Sans", Arial, sans-serif;
  }
  .canvas { position: relative; width: 968px; height: 1200px; }
  .sheet {
    position: absolute; left: 64px; top: 17px;
    width: 750px; height: 1041px;
    background: var(--paper);
    transform: scale(1.12); transform-origin: 0 0;
  }
  .bar-top { position: absolute; left: 0; top: 0; width: 151px; height: 9px; background: var(--dark); }
  .title {
    position: absolute; left: 57px; top: 60px;
    font-size: 52px; font-weight: 400; color: var(--accent); letter-spacing: 0.5px; line-height: 1.1;
  }
  .subtitle {
    position: absolute; left: 58px; top: 122px;
    font-size: 30px; font-weight: 400; color: var(--heading-grey); letter-spacing: 1px; line-height: 1.2;
  }
  .intro {
    position: absolute; left: 59px; top: 186px; width: 640px;
    font-size: 15.5px; line-height: 23.5px; color: var(--text); letter-spacing: 0.55px;
  }
  .product {
    position: absolute; top: 306px; width: 220px; margin-left: -110px;
    text-align: center; color: var(--text); font-size: 13.5px; letter-spacing: 0.4px;
  }
  .product-visual {
    height: 92px; margin: 0 auto;
    border-radius: 6px 6px 14px 14px;
    background: linear-gradient(180deg, var(--device-light) 0%, var(--device-mid) 55%, var(--device-light) 100%);
  }
  .product-name { margin-top: 18px; font-weight: 600; line-height: 18px; }
  .product-specs { margin-top: 17px; line-height: 17.5px; }
  .photo {
    position: absolute; left: 17px; top: 583px; width: 733px; height: 282px;
    background: radial-gradient(ellipse at 62% 35%, var(--photo-light) 0%, var(--photo-copper) 35%, var(--photo-dark) 80%);
  }
  .references {
    position: absolute; left: 18px; top: 940px; width: 720px; height: 60px;
    display: flex; align-items: center; justify-content: space-between;
    color: var(--dark); font-size: 16px; font-weight: 600; letter-spacing: 0.5px;
  }
  .reference { display: flex; align-items: center; gap: 8px; }
  .reference-mark { width: 12px; height: 12px; background: var(--dark); }
  .bar-bottom-accent { position: absolute; left: 0; top: 1031px; width: 563px; height: 10px; background: var(--accent); }
  .bar-bottom-dark { position: absolute; left: 574px; top: 1031px; width: 176px; height: 10px; background: var(--dark); }
</style>
</head>
<body>
<div class="canvas">
  <article class="sheet">
    <div class="bar-top"></div>
    <h1 class="title">Gastroschankanlagen</h1>
    <h2 class="subtitle">MORAFI NG Full-Color-Touch</h2>
    <p class="intro">Übersichtliche Managerfunktionen&nbsp; und Auswertungen Kredit-, Debit- bzw. Mischbetrieb mit Kreditanzeige sowie Bierpool&nbsp; und Mini-Touchkassenfunk-tion&nbsp; möglich Anschluss von Fremdgeräten wie Kaffeemaschinen usw. möglich</p>

    <section class="product" style="left:135px">
      <div class="product-visual" style="width:148px" role="img" aria-label="Schankanlage Full-Color-Touch, Produktfoto"></div>
      <div class="product-name">Full-Color-Touch<br>8-leitig</div>
      <div class="product-specs">Breite 740 mm<br>Höhe 557 mm<br>Tiefe 393 mm</div>
    </section>
    <section class="product" style="left:365px">
      <div class="product-visual" style="width:166px" role="img" aria-label="Schankanlage Full-Color-Touch, Produktfoto"></div>
      <div class="product-name">Full-Color-Touch<br>8-leitig</div>
      <div class="product-specs">Breite 740 mm<br>Höhe 557 mm<br>Tiefe 393 mm</div>
    </section>
    <section class="product" style="left:591px">
      <div class="product-visual" style="width:202px" role="img" aria-label="Schankanlage Full-Color-Touch, Produktfoto"></div>
      <div class="product-name">Full-Color-Touch<br>8-leitig</div>
      <div class="product-specs">Breite 740 mm<br>Höhe 557 mm<br>Tiefe 393 mm</div>
    </section>

    <div class="photo" role="img" aria-label="Nahaufnahme von Zapfhähnen an einer kupfernen Schankanlage"></div>

    <footer class="references">
      <span class="reference"><span class="reference-mark"></span>Casa Lumi</span>
      <span class="reference">Helena Brinz</span>
      <span class="reference">Velden Restaurants</span>
      <span class="reference">Barcella</span>
    </footer>

    <div class="bar-bottom-accent"></div>
    <div class="bar-bottom-dark"></div>
  </article>
</div>
</body>
</html>
```